Goldschmiede sucht Flyer mit GUtschein abriss
Zielgruppe
ICh bin ein Goldschmied in Saarbrücken Trier und Mainz und mache jegliche Dienstleistungen eines Goldschmiedes.Es sollen noch mit ein paar passenden Fotos gearbeitet werden.
Aufgabenstellung
Ich suche einen Flyer für meine Goldschmiede vorhandene Punkte sollen sein.
Reparaturen aller Art , Ringweitenänderung, Löten , Polieren / Aufarbeiten , Neuanfertigung nach Wunsch ,Rhodienieren , Gravieren , usw.
Der Flyer soll am unteren Rand die Möglichkeit haben, abgeschnitten zu werden dort soll ein Gutschein entstehen zb. mit 20 % Rabatt.
( der Abriss soll nummeriert werden damit niemand kopiert oder mehrfach abgibt )
Auf der Internetseite können Sie sich meine Firmenfarben ansehen in diesen Farben soll auch das Flyer-Design sein.
Bei der Adresse sollen alle drei Filialen angegeben werden.

```html
<!DOCTYPE html>
<html lang="de">
<head>
<meta charset="utf-8">
<title>Matthias Lorenz Goldschmiede – Flyer</title>
<link href="https://fonts.googleapis.com/css2?family=Montserrat:wght@400;500;600;700&display=swap" rel="stylesheet">
<style>
  :root {
    --gold: #b8995a;
    --gold-light: #e6c35a;
    --gold-dark: #9b7d3c;
    --slate: #48484e;
    --slate-deep: #3c3c40;
    --ink: #3d3d42;
    --white: #ffffff;
  }
  * { margin: 0; padding: 0; box-sizing: border-box; }
  html, body { width: 846px; height: 1200px; overflow: hidden; background: var(--white); }
  body { font-family: "Montserrat", Arial, sans-serif; }
  .flyer { position: relative; width: 846px; height: 1200px; background: var(--white); overflow: hidden; }
  .gold-rule { position: absolute; left: 0; width: 846px; background: linear-gradient(90deg, var(--gold-dark), var(--gold-light) 50%, var(--gold) ); }
  .rule-top { top: 21px; height: 6px; }
  .rule-header { top: 260px; height: 7px; }
  .rule-main { top: 855px; height: 8px; }
  .rule-bottom { top: 1189px; height: 11px; }

  .header { position: absolute; top: 35px; left: 0; width: 846px; height: 220px; background: var(--slate); }
  .brand { position: absolute; top: 62px; left: 0; width: 846px; text-align: center; color: var(--gold); font-weight: 500; }
  .brand-mark { display: block; width: 14px; height: 14px; background: var(--gold); margin: 0 auto 16px; }
  .brand-name { display: block; font-size: 36px; letter-spacing: 2px; }
  .brand-sub { display: block; font-size: 17px; letter-spacing: 7px; margin-top: 10px; text-transform: uppercase; }

  .services-panel { position: absolute; top: 267px; left: 0; width: 846px; height: 588px; background: var(--slate); }
  .service-list { position: absolute; top: 100px; left: 38px; list-style: none; }
  .service-list li { display: flex; align-items: center; height: 40.3px; font-size: 24px; font-weight: 600; letter-spacing: 0.6px; color: var(--white); }
  .service-list li:nth-child(odd) { color: var(--gold); }
  .service-list svg { width: 26px; height: 14px; margin-right: 13px; flex: none; }
  .faint { color: #55555b; }
  .ring-photo { position: absolute; left: 546px; top: 230px; width: 300px; height: 345px;
    background: radial-gradient(ellipse at 45% 45%, #f2b36a 0%, #c9853d 35%, #8c6a45 60%, rgba(72,72,78,0) 75%); }

  .branches { position: absolute; top: 871px; left: 0; width: 846px; height: 129px; background: linear-gradient(180deg, #4a4a4e, #3f3f43); display: flex; }
  .branch { position: absolute; top: 17px; font-size: 17.5px; line-height: 21.6px; color: #e8e8e8; }
  .branch h3 { font-size: 17px; font-weight: 700; color: var(--gold); letter-spacing: 0.3px; }
  .branch-sb { left: 48px; } .branch-tr { left: 338px; } .branch-mz { left: 640px; }
  .divider { position: absolute; top: 28px; width: 1px; height: 64px; background: var(--gold); }
  .divider-a { left: 269px; } .divider-b { left: 577px; }

  .coupon { position: absolute; top: 1000px; left: 0; width: 846px; height: 134px; background: var(--white); }
  .jewellery-photo { position: absolute; left: 0; top: 0; width: 392px; height: 134px;
    background: linear-gradient(100deg, #6b4a12 0%, #c79a35 30%, #e8c46a 50%, #a67a22 70%, #d9cdb3 100%); }
  .coupon-art { position: absolute; left: 0; top: -20px; width: 846px; height: 154px; overflow: visible; }
  .discount { position: absolute; left: 418px; top: 10px; font-size: 68px; font-weight: 700; color: var(--white); letter-spacing: 1px; }
  .coupon-no { position: absolute; left: 441px; top: 102px; font-size: 19px; font-weight: 500; color: var(--ink); letter-spacing: 1px; }
  .coupon-title { position: absolute; left: 624px; top: 16px; font-size: 48px; font-weight: 500; color: var(--ink); letter-spacing: 1.5px; }
  .coupon-text { position: absolute; left: 624px; top: 70px; color: var(--ink); font-weight: 500; }
  .coupon-text span { display: block; }
  .coupon-text .l1 { font-size: 26px; letter-spacing: 1.4px; line-height: 28px; }
  .coupon-text .l2 { font-size: 20.5px; letter-spacing: 1.2px; line-height: 26px; }

  .hours { position: absolute; top: 1134px; left: 0; width: 846px; height: 52px; background: #404044; text-align: center;
    line-height: 52px; font-size: 16.5px; font-weight: 600; color: var(--white); letter-spacing: 0.2px; }
  .hours b { color: var(--gold); font-weight: 600; }
</style>
</head>
<body>
<div class="flyer">
  <div class="gold-rule rule-top"></div>

  <header class="header">
    <div class="brand">
      <span class="brand-mark"></span>
      <span class="brand-name">Matthias Lorenz</span>
      <span class="brand-sub">Goldschmiede</span>
    </div>
  </header>
  <div class="gold-rule rule-header"></div>

  <section class="services-panel">
    <ul class="service-list">
      <li><svg viewBox="0 0 26 14"><path d="M2 7h20M16 2l6 5-6 5" fill="none" stroke="currentColor" stroke-width="2"/></svg>REPARATUREN ALLER ART</li>
      <li><svg viewBox="0 0 26 14"><path d="M2 7h20M16 2l6 5-6 5" fill="none" stroke="currentColor" stroke-width="2"/></svg>RINGWEITENÄNDER<span class="faint">UNG</span></li>
      <li><svg viewBox="0 0 26 14"><path d="M2 7h20M16 2l6 5-6 5" fill="none" stroke="currentColor" stroke-width="2"/></svg>LÖTEN</li>
      <li><svg viewBox="0 0 26 14"><path d="M2 7h20M16 2l6 5-6 5" fill="none" stroke="currentColor" stroke-width="2"/></svg>POLIEREN / AUFARBEITEN</li>
      <li><svg viewBox="0 0 26 14"><path d="M2 7h20M16 2l6 5-6 5" fill="none" stroke="currentColor" stroke-width="2"/></svg>NEUANFERTIGUNG NACH WUNSCH</li>
      <li><svg viewBox="0 0 26 14"><path d="M2 7h20M16 2l6 5-6 5" fill="none" stroke="currentColor" stroke-width="2"/></svg>RHODENIEREN</li>
      <li><svg viewBox="0 0 26 14"><path d="M2 7h20M16 2l6 5-6 5" fill="none" stroke="currentColor" stroke-width="2"/></svg>GRAVIEREN</li>
      <li><svg viewBox="0 0 26 14"><path d="M2 7h20M16 2l6 5-6 5" fill="none" stroke="currentColor" stroke-width="2"/></svg>UND VIELES MEHR</li>
    </ul>
    <div class="ring-photo" role="img" aria-label="Foto: zwei gravierte goldene Eheringe"></div>
  </section>
  <div class="gold-rule rule-main"></div>

  <section class="branches">
    <div class="branch branch-sb"><h3>SAARBRÜCKEN</h3><p>Lindenallee 7</p><p>66113 Saarbrücken</p><p>Tel: 0681 - 41 205 360</p></div>
    <div class="divider divider-a"></div>
    <div class="branch branch-tr"><h3>TRIER</h3><p>Weidenweg 4</p><p>54292 Trier</p><p>Tel: 0651 - 37 620 418</p></div>
    <div class="divider divider-b"></div>
    <div class="branch branch-mz"><h3>MAINZ</h3><p>Rosenplatz 9</p><p>55118 Mainz</p><p>Tel: 06131 - 518 33 70</p></div>
  </section>

  <section class="coupon">
    <div class="jewellery-photo" role="img" aria-label="Foto: goldener Schmuck mit Perle und Steinen"></div>
    <svg class="coupon-art" viewBox="0 0 846 154" aria-hidden="true">
      <defs>
        <linearGradient id="ribbon" x1="0" x2="1" y1="0" y2="0">
          <stop offset="0" stop-color="#a8894a"/><stop offset="0.6" stop-color="#c9a95e"/><stop offset="1" stop-color="#e7c25a"/>
        </linearGradient>
      </defs>
      <line x1="576" y1="21" x2="846" y2="21" stroke="#6a6a70" stroke-width="1.5" stroke-dasharray="5 4"/>
      <path d="M390 21 H570 L612 64 L570 109 H418 V154 H418 C400 150 388 140 388 124 V21 Z" fill="url(#ribbon)"/>
      <path d="M418 109 V154 C400 150 388 140 390 118 C396 108 406 108 418 109 Z" fill="#8e7238"/>
      <g stroke="#a8894a" stroke-width="2.2" fill="none" transform="translate(792,4)">
        <circle cx="36" cy="4" r="4"/><circle cx="36" cy="24" r="4"/>
        <path d="M33 7 L2 20 M33 21 L2 8"/>
      </g>
    </svg>
    <div class="discount">20 %</div>
    <div class="coupon-no">NR: 66565</div>
    <div class="coupon-title">RABATT</div>
    <div class="coupon-text"><span class="l1">auf alle Gold-</span><span class="l2">schmiedearbeiten</span></div>
  </section>

  <footer class="hours"><b>ÖFFNUNGSZEITEN:</b> MO - FR 9:30 BIS 18:00 UHR UND SA 9:30 BIS 14:00 UHR</footer>
  <div class="gold-rule rule-bottom"></div>
</div>
</body>
</html>
```